Marlowe's Classic Dressing

We are looking for a new label as we switch or glass bottle from a traditional bottle to a round bottle. We want to create a newer/ more appealing logo, while still maintaining some of our old label features to ensure that the brand awareness is not lost. We like the coloring of the blue and white, but feel free to play around with other colors in the design.
We are looking to add product features to our label such as "Gluten-Free", "Original Recipe From 1957" "Family Owned". With this being an older company we would like to keep the traditional feel of our label with some added modern touches.
We are not married to the greek logo/ building but would love some designs with and without it.
WE ARE LOOKING FOR A ROUND LABEL. The pictures provided below are of the old bottle.
There is a picture of the ringneck bottle below. The size of the label is 4.00 x 7.00.

```html
<!DOCTYPE html>
<html lang="en">
<head>
<meta charset="utf-8">
<title>Marlowe's Greek Dressing Label</title>
<link rel="stylesheet" href="https://fonts.googleapis.com/css2?family=Libre+Baskerville&family=Open+Sans:ital,wght@0,600;1,500&family=Roboto+Condensed:wght@400&display=swap">
<style>
  :root {
    --label-blue: #3f63b6;
    --label-sand: #d8d2c2;
    --label-white: #ffffff;
    --art-light: #dfe3ea;
    --art-dark: #8e96a3;
  }
  html, body {
    margin: 0;
    width: 714px;
    height: 1200px;
    overflow: hidden;
    background: var(--label-white);
  }
  .label { display: block; width: 714px; height: 1200px; }
  .oval-ring { fill: var(--label-sand); }
  .oval-field { fill: var(--label-blue); }
  .title-band { fill: var(--label-sand); }
  .ribbon { fill: var(--label-sand); }
  .ribbon-text {
    font-family: "Open Sans", sans-serif;
    font-style: italic;
    font-weight: 500;
    font-size: 25px;
    fill: var(--label-blue);
  }
  .brand-name {
    font-family: "Open Sans", sans-serif;
    font-weight: 600;
    font-size: 62px;
    fill: var(--label-white);
  }
  .product-type {
    font-family: "Libre Baskerville", serif;
    font-size: 116px;
    letter-spacing: 4px;
    fill: var(--label-blue);
  }
  .product-kind {
    font-family: "Open Sans", sans-serif;
    font-weight: 600;
    font-size: 47px;
    letter-spacing: 4px;
    fill: var(--label-blue);
  }
  .feature {
    font-family: "Open Sans", sans-serif;
    font-style: italic;
    font-weight: 500;
    font-size: 29px;
    fill: var(--label-white);
  }
  .volume {
    font-family: "Roboto Condensed", sans-serif;
    font-size: 27px;
    fill: var(--label-white);
  }
</style>
</head>
<body>
<svg class="label" viewBox="0 0 714 1200" xmlns="http://www.w3.org/2000/svg">
  <defs>
    <clipPath id="field-clip">
      <ellipse cx="357" cy="597" rx="303" ry="540"/>
    </clipPath>
    <linearGradient id="temple-tone" x1="0" y1="0" x2="0" y2="1">
      <stop offset="0" stop-color="var(--art-light)"/>
      <stop offset="1" stop-color="var(--art-dark)"/>
    </linearGradient>
  </defs>

  <ellipse class="oval-ring" cx="357" cy="597" rx="333" ry="569"/>
  <ellipse class="oval-field" cx="357" cy="597" rx="303" ry="540"/>

  <g clip-path="url(#field-clip)">
    <rect class="title-band" x="0" y="493" width="714" height="240"/>
  </g>

  <rect class="temple-art" role="img" aria-label="Illustration of an ancient Greek temple with columns"
        x="240" y="145" width="234" height="100" rx="4" fill="url(#temple-tone)"/>

  <g class="recipe-ribbon">
    <path class="ribbon" d="M226 264 L532 250 L538 298 L232 312 Z"/>
    <text class="ribbon-text" x="382" y="290" text-anchor="middle" transform="rotate(-2.6 382 283)">Original Recipe From 1957</text>
  </g>

  <text class="brand-name" x="357" y="444" text-anchor="middle">Marlowe's</text>

  <text class="product-type" x="357" y="631" text-anchor="middle">GREEK</text>
  <text class="product-kind" x="357" y="712" text-anchor="middle">DRESSING</text>

  <text class="feature" x="357" y="855" text-anchor="middle">Gluten-Free</text>
  <text class="feature" x="357" y="909" text-anchor="middle">Family Owned</text>

  <text class="volume" x="357" y="1022" text-anchor="middle">8 FL. OZ. (237 ml)</text>
</svg>
</body>
</html>
```